2018 Vision Board Workshop

I need to promote this workshop on both an 8.5x11 sheet and a 5x7 card. I do have a logo that needs to be present. I'd like to stay true to my branded colors. The flyer needs to project the excitement of a new year and the possibilities of what a person can create, produce, explore in their lives by putting it all on a vision board. Creating the vision of what you want will inspire you to achieve your goals and dreams. Looking at your vision board each day will propel you into taking action as you chart your course to achieve what you truly want.
The flyer needs to have the following information:
The workshop date and time - Sat., Jan. 13, 2018, 10:30-1:30
The location is - Lantern Hall 7B, 2648 Maple Ridge Dr, Colorado Springs, Co 80920
in the FORGE Room
My name and contact information - Laura Pendleton
Text and voice 303-555-0147
Email - laura@joy-grows-daily.example
Website - joy-grows-daily.example
The fee is $45. All materials are provided.

My company is called Joy Grows Daily. I am a Life Coach, author, speaker and workshop leader.\ I wrote this program, Joy Grows Daily to teach concepts and supporting skills for living with more happiness, satisfaction and fulfillment. Thanks for reading this!! Laura

Target Market(s)

Primarily women, educated, motivated, proactive in their own lives and well being

Font styles to use
Other font styles liked:
• I have been using Century Gothic. I'm open to new ideas.

Requirements
Must have
• The Joy Grows Daily logo
• The flyer needs to have the following information:
• The workshop date and time - Sat., Jan. 13, 2018, 10:30-1:30
• The location is - Lantern Hall 7B, 2648 Maple Ridge Dr, Colorado Springs, Co 80920
• in the FORGE Room
• My name and contact information - Laura Pendleton
• Text and voice 303-555-0147
• Email - laura@joy-grows-daily.example
• Website - joy-grows-daily.example
• The fee is $45. All materials are provided.
Nice to have
• The Joy Grows Daily branded colors in the design
• Images of vision boards

```html
<!DOCTYPE html>
<html lang="en">
<head>
<meta charset="utf-8">
<title>2018 Vision Board Workshop</title>
<link rel="stylesheet" href="https://fonts.googleapis.com/css2?family=Questrial&family=Mulish:wght@400;700;800&display=swap">
<style>
  :root{
    --green:#8fd400;
    --green-bright:#99dd00;
    --navy:#0b3a9e;
    --ink:#4a4a4a;
    --dark:#2e2e2e;
    --sky:#29a8e0;
    --chip:#dcdcdc;
    --contact:#1f2f6b;
    --page:#f2f2f2;
  }
  *{margin:0;padding:0;box-sizing:border-box}
  html,body{width:1200px;height:1200px;overflow:hidden;background:var(--page)}
  .canvas{position:relative;width:1200px;height:1200px;overflow:hidden}
  .flyer{position:absolute;left:136px;top:0;width:998px;height:1292px;transform:scale(0.9288);transform-origin:0 0;overflow:hidden;font-family:"Mulish",sans-serif;box-shadow:0 0 12px rgba(0,0,0,.15)}
  .backdrop{position:absolute;inset:0}
  .abs{position:absolute}
  .lockup{left:60px;top:470px;display:inline-flex;flex-direction:column;align-items:flex-end}
  .brand-name{font-family:"Questrial",sans-serif;font-size:64px;line-height:70px;color:var(--green);white-space:nowrap;letter-spacing:1px}
  .tagline{font-family:"Questrial",sans-serif;font-size:19px;line-height:22px;color:var(--sky);letter-spacing:1px;white-space:nowrap}
  .title-year{left:100px;top:596px;font-family:"Mulish",sans-serif;font-weight:800;font-size:66px;color:var(--navy);letter-spacing:-2px;white-space:nowrap}
  .title-main{left:44px;top:670px;font-family:"Questrial",sans-serif;font-weight:400;font-size:70px;color:var(--ink);letter-spacing:-1px;white-space:nowrap}
  .blooms{left:24px;top:780px;width:430px;height:240px;border-radius:50%;background:radial-gradient(ellipse at 45% 50%,rgba(33,170,255,.55) 0%,rgba(33,170,255,.25) 55%,rgba(33,170,255,0) 75%)}
  .details-head{left:622px;top:538px;font-weight:700;font-size:22px;color:var(--dark);white-space:nowrap}
  .chip{left:676px;background:var(--chip);color:var(--dark);font-weight:700;font-size:18px;padding:0 12px;line-height:22px}
  .chip-date{top:580px;width:286px;height:33px;display:flex;align-items:center;white-space:nowrap}
  .chip-place{top:631px;width:286px;padding-top:4px;padding-bottom:4px;font-size:16.5px;line-height:21.5px}
  .icon{position:absolute}
  .host-label{left:689px;top:722px;font-family:"Questrial",sans-serif;font-size:22px;color:var(--ink);border-bottom:1.5px solid var(--ink);line-height:26px}
  .host-name{left:689px;top:754px;font-weight:800;font-size:32px;color:var(--navy);letter-spacing:-1px;white-space:nowrap}
  .portrait{left:662px;top:812px;width:268px;height:300px;border-radius:120px 120px 0 0}
  .fee{left:56px;top:1000px;width:270px;height:270px;display:flex;flex-direction:column;align-items:center;justify-content:center;text-align:center;font-family:"Questrial",sans-serif;color:var(--dark)}
  .fee-lead{font-size:38px;line-height:40px}
  .fee-amount{font-family:"Mulish",sans-serif;font-weight:800;font-size:50px;color:var(--navy);line-height:56px;letter-spacing:-1px}
  .fee-note{font-size:25px;line-height:30px;margin-top:4px}
  .contacts{right:66px;top:1145px;list-style:none;text-align:right}
  .contacts li{display:flex;justify-content:flex-end;align-items:center;gap:18px;height:38.5px;font-weight:700;font-size:20px;color:var(--contact);white-space:nowrap}
  .contacts svg{width:20px;height:20px}
</style>
</head>
<body>
<div class="canvas">
  <div class="flyer">
    <svg class="backdrop" width="998" height="1292" viewBox="0 0 998 1292" aria-hidden="true">
      <defs>
        <linearGradient id="paper" x1="0" y1="0" x2="0" y2="1">
          <stop offset="0" stop-color="#ffffff"/>
          <stop offset="1" stop-color="#e4e4e4"/>
        </linearGradient>
        <linearGradient id="crowd" x1="0" y1="0" x2="1" y2="1">
          <stop offset="0" stop-color="#e9e9e6"/>
          <stop offset="0.5" stop-color="#c9b6a3"/>
          <stop offset="1" stop-color="#a69484"/>
        </linearGradient>
      </defs>
      <rect width="998" height="1292" fill="url(#paper)"/>
      <rect width="998" height="520" fill="url(#crowd)" role="img" aria-label="Photo of a smiling, diverse group of adults standing together"/>
      <path d="M0,340 C110,300 240,280 380,300 C560,330 720,450 998,410 L998,500 C850,525 720,470 600,420 C450,350 250,300 0,430 Z" fill="var(--green-bright)"/>
      <path d="M0,430 C250,300 450,350 600,420 C720,470 850,525 998,500 L998,1292 L0,1292 Z" fill="url(#paper)"/>
    </svg>

    <div class="abs blooms" role="img" aria-label="Decorative blue lotus flowers"></div>

    <div class="abs portrait" role="img" aria-label="Portrait photo of the workshop leader, Laura Pendleton" style="background:linear-gradient(180deg,#d9c7a8 0%,#e6c3ad 45%,#8ccfc9 80%,#7cc4bd 100%)"></div>

    <svg class="backdrop" width="998" height="1292" viewBox="0 0 998 1292" aria-hidden="true">
      <path d="M0,1292 L0,1135 C40,1070 120,1040 190,1050 C300,1060 400,1170 490,1222 C600,1140 720,1090 860,1082 C930,1080 975,1100 998,1130 L998,1292 Z" fill="var(--green-bright)"/>
      <path d="M32,1292 C50,1215 120,1185 210,1190 C300,1195 390,1240 430,1292 Z" fill="#ffffff"/>
      <path d="M18,1145 A173,173 0 0 1 364,1145" fill="none" stroke="var(--navy)" stroke-width="5"/>
      <circle cx="191" cy="1135" r="150" fill="var(--green-bright)"/>
      <circle cx="191" cy="1135" r="136" fill="none" stroke="var(--navy)" stroke-width="5"/>
    </svg>

    <div class="abs lockup">
      <div class="brand-name">Joy Grows Daily</div>
      <div class="tagline">Small steps lead to brighter days</div>
    </div>

    <h1 class="abs title-year">2018 VISION</h1>
    <h2 class="abs title-main">Board Workshop</h2>

    <div class="abs details-head">The workshop date and time</div>
    <svg class="icon" style="left:630px;top:583px" width="34" height="34" viewBox="0 0 34 34" aria-hidden="true">
      <rect x="2" y="5" width="22" height="20" rx="2" fill="none" stroke="var(--navy)" stroke-width="2.5"/>
      <rect x="2" y="5" width="22" height="6" fill="var(--navy)"/>
      <rect x="6" y="1" width="3" height="6" fill="var(--navy)"/>
      <rect x="17" y="1" width="3" height="6" fill="var(--navy)"/>
      <circle cx="24" cy="24" r="8" fill="#fff" stroke="var(--navy)" stroke-width="2.5"/>
      <path d="M24 19 V24 H28" fill="none" stroke="var(--navy)" stroke-width="2"/>
    </svg>
    <div class="abs chip chip-date">Sat, Jan. 13, 2018,10:30-1:30</div>

    <svg class="icon" style="left:638px;top:633px" width="20" height="28" viewBox="0 0 20 28" aria-hidden="true">
      <path d="M10 1 C4.5 1 1 5 1 10 C1 17 10 27 10 27 C10 27 19 17 19 10 C19 5 15.5 1 10 1 Z" fill="var(--navy)"/>
      <circle cx="10" cy="10" r="3.5" fill="#fff"/>
    </svg>
    <div class="abs chip chip-place">Lantern Hall 7B, 2648 Maple Ridge Dr, Colorado Springs, Co 80920 in the FORGE Room</div>

    <div class="abs host-label">My name</div>
    <div class="abs host-name">Laura Pendleton</div>

    <div class="abs fee">
      <div class="fee-lead">The fee is</div>
      <div class="fee-amount">$45</div>
      <div class="fee-note">All materials are<br>provided</div>
    </div>

    <ul class="abs contacts">
      <li>303-555-0147
        <svg viewBox="0 0 20 20" aria-hidden="true"><path d="M5 2 L8 6 L6 8 C7 11 9 13 12 14 L14 12 L18 15 L16 18 C9 18 2 11 2 4 Z" fill="var(--navy)"/></svg>
      </li>
      <li>joy-grows-daily.example
        <svg viewBox="0 0 20 20" aria-hidden="true"><circle cx="10" cy="10" r="8" fill="none" stroke="var(--navy)" stroke-width="2"/><path d="M2 10 H18 M10 2 C6 6 6 14 10 18 M10 2 C14 6 14 14 10 18" fill="none" stroke="var(--navy)" stroke-width="1.6"/></svg>
      </li>
      <li>laura@joy-grows-daily.example
        <svg viewBox="0 0 20 20" aria-hidden="true"><rect x="2" y="5" width="16" height="11" rx="1" fill="var(--navy)"/><path d="M2 6 L10 12 L18 6" fill="none" stroke="#fff" stroke-width="1.6"/></svg>
      </li>
    </ul>
  </div>
</div>
</body>
</html>
```